Harbor Sushi & Steak Dinner Menu

I'm looking for a MENU design with a particular feel. I want to have a base template made that I can then use for future alterations to the menu; ie I can go in and change out different entrees as the menu changes but the template will remain the same. (Ideally it would be in an Apple Pages format.). Also ideally - dinner menu will occupy 2 pages 8.5 x 11. The restaurant's name is Harbor. It is a MODERN steak house that will also feature Sushi, a Raw Bar, Exquisite Cocktails and a sophisticated nightlife crowd. I have attached our LOGO, a secondary logo that we will be featuring throughout the project including on the menu cover (the gold U). Finally - I have attached the content that we would like to see. AGAIN - I REITERATE: High end dining and lounge atmosphere. A couple of restaurants / menus that I love are Morvendel in NYC and Pellucid Steakhouse in Long Island NY. Please do not duplicate - just trying to offer some suggestions.

Requirements
Must have
• A sophisticated and elegant feel without being stuffy or old.

```html
<!DOCTYPE html>
<html lang="en">
<head>
<meta charset="utf-8">
<title>Harbor Sushi &amp; Steak — Dinner Menu</title>
<link rel="stylesheet" href="https://fonts.googleapis.com/css2?family=Josefin+Sans:wght@300;400;700&display=swap">
<style>
  :root {
    --backdrop: #e6e6e6;
    --cover-red: #c4323f;
    --cover-ink: #f3c9c6;
    --page-paper: #f4f3f1;
    --heading-red: #b3242f;
    --body-ink: #2a2a2a;
    --muted-ink: #6d6d6d;
    --gold: #d9b25a;
    --gold-soft: #ecd9a6;
  }
  * { box-sizing: border-box; margin: 0; padding: 0; }
  html, body {
    width: 1200px; height: 900px; overflow: hidden;
    background: var(--backdrop);
    font-family: "Josefin Sans", sans-serif;
  }
  .spread {
    position: absolute; left: 170px; top: 178px;
    display: flex; gap: 20px;
  }
  .page {
    width: 420px; height: 543px; position: relative; overflow: hidden;
  }
  /* Cover */
  .cover {
    background: var(--cover-red);
    display: flex; align-items: center; justify-content: center;
  }
  .cover-name {
    color: var(--cover-ink);
    font-weight: 400;
    font-size: 64px;
    letter-spacing: 8px;
    margin-top: -60px;
  }
  /* Inside page */
  .inside { background: var(--page-paper); }
  .photo-sushi {
    position: absolute; right: 0; top: 0; width: 240px; height: 200px;
    background: linear-gradient(135deg, #f2f2f0 0%, #dcdad6 45%, #2d2a28 70%, #e4c26a 85%, #f5f5f3 100%);
  }
  .roll-note {
    position: absolute; left: 24px; top: 70px; width: 140px;
    font-size: 11px; line-height: 1.55; color: var(--muted-ink);
  }
  .section-title {
    position: absolute; left: 24px; top: 216px;
    font-weight: 700; font-size: 26px; letter-spacing: 1.5px;
    color: var(--heading-red);
  }
  .title-bar {
    position: absolute; right: 36px; top: 250px; width: 40px; height: 12px;
    background: var(--gold-soft);
  }
  .raw-bar-list {
    position: absolute; right: 60px; top: 272px; list-style: none; text-align: right;
  }
  .raw-bar-list li {
    font-size: 13px; font-weight: 700; color: var(--body-ink);
    line-height: 1.6; display: flex; align-items: center; justify-content: flex-end; gap: 10px;
  }
  .price-mark {
    display: inline-block; width: 7px; height: 7px; background: var(--gold);
  }
  .platter-note {
    position: absolute; left: 24px; right: 30px; top: 384px;
    font-size: 11px; line-height: 1.55; color: var(--muted-ink);
  }
  .photo-seafood {
    position: absolute; left: 0; bottom: 0; width: 250px; height: 105px;
    border-top-right-radius: 125px;
    background: radial-gradient(ellipse at 45% 70%, #e8834f 0%, #c9632f 30%, #5a4a2c 55%, #eaeae8 85%);
  }
</style>
</head>
<body>
  <main class="spread">
    <section class="page cover" aria-label="Menu cover">
      <h1 class="cover-name">HARBOR</h1>
    </section>
    <section class="page inside" aria-label="Seafood raw bar page">
      <div class="photo-sushi" role="img" aria-label="Photo of sliced sushi rolls on a white plate with dipping sauce and chopsticks"></div>
      <p class="roll-note">Crab, avocado and cucumber rolled in rice, finished with spicy mayo and seared salmon on top.</p>
      <h2 class="section-title">SEAFOOD RAW BAR</h2>
      <div class="title-bar"></div>
      <ul class="raw-bar-list">
        <li>Lobster Cocktail <span class="price-mark"></span></li>
        <li>Shrimp Cocktail <span class="price-mark"></span></li>
        <li>Clams on the Half Shell <span class="price-mark"></span></li>
        <li>Oysters on the Half Shell <span class="price-mark"></span></li>
        <li>Colossal Crab Cocktail <span class="price-mark"></span></li>
      </ul>
      <p class="platter-note">Grand Platter: half of a One Pound Lobster, two Shrimp, one East Coast Oyster, one West Coast Oyster.</p>
      <div class="photo-seafood" role="img" aria-label="Photo of a seafood platter with mussels, prawns, crab and lemon"></div>
    </section>
  </main>
</body>
</html>
```